Stationery Design Project for Marketing Consultancy

I have started a new consultancy business and require the following elements to be designed using existing logo:
• Business card
• Letterhead
• Envelope (DL, C4, C5)
• Microsoft word template for report writing
• A4 Presentation Folder
• Powerpoint template
COPY FOR FRONT AND BACK OF BUSINESS CARD
logo
'Measurable Marketing. Epic Results' slogan (but no need to use existing lockup with logo)
name, B Bus. Mktg, Grad Dip Digital Mktg, CPM (post nominal abbreviations in smaller font)
mobile: 04XX-XXX-XXX (I will give details to the winner to add)
website: www.quorvial.com.au
email: info@quorvial.com.au
COPY FOR LETTERHEAD
Logo
Company Name
Please, submit your designs that include business card, letterhead and envelope. Once selected the winner will be asked to complete the project by creating the rest of the artwork.
FINAL FILES
Print ready files to be supplied as well as Indesign files so that minor amends can be made if necessary in future.
• Layered vectors in EPS & PDF
• Screen quality JPEG & PNGs
ABOUT THE BUSINESS: QUORVIAL
I work with clients to understand their business challenges, developing and executing measurable marketing strategies tied to key business metrics. Services include:
Services include:
• Business planning and business development
• Marketing and brand strategy
• Insight-driven integrated campaigns
• Loyalty programs and retention marketing
• Marketing automation
• Direct marketing (traditional and digital)
• Content strategy and development
Hi everyone,
Target Market(s)
Corporate decision makers (heads of marketing, general managers etc) and small to medium sized business owners. Predominately male aged 35+
Industry/Entity Type
Marketing
Requirements
Must have
- BRAND PERSONALITY
The successful design will communicate brand personality. I am a professional, results-driven entrepreneur, but want to show off my creative flair.
MEMORABILITY
Looking for a unique and eye-catching design. Am considering special printing effects (die cuts, letterpress, interactive elements, embossing, foiling etc) or a striking minimalist approach.
Nice to have
- I have a mission that could be incorporated on reverse if room -
Turning insights into actions & passion into profit.
Should not have
- Use of pink or green.

```html
<!DOCTYPE html>
<html lang="en">
<head>
<meta charset="utf-8">
<title>Quorvial — Business Card Concepts</title>
<link rel="stylesheet" href="https://fonts.googleapis.com/css2?family=PT+Sans:wght@400;700&display=swap">
<style>
  :root {
    --brand-blue: #0a2dbb;
    --brand-navy: #0e1a4f;
    --card-paper: #f1f1f1;
    --ink-grey: #3b3b3b;
    --text-grey: #4a4a4a;
    --silver: #cfcfcf;
    --page: #ffffff;
  }
  * { margin: 0; padding: 0; box-sizing: border-box; }
  html, body {
    width: 1200px; height: 907px; overflow: hidden;
    background: var(--page);
    font-family: "PT Sans", "Myriad Pro", Arial, sans-serif;
  }
  .sheet { position: relative; width: 1200px; height: 907px; }

  .card {
    position: absolute; width: 473px; height: 277px;
    background: var(--card-paper);
    box-shadow: 2px 3px 6px rgba(0,0,0,0.22);
    overflow: hidden;
  }
  .card--front-bold { left: 83px; top: 188px; }
  .card--front-quiet { left: 645px; top: 188px; }
  .card--back-grey { left: 83px; top: 501px; }
  .card--back-navy { left: 645px; top: 501px; }

  .brand-panel {
    position: absolute; left: 0; top: 0; width: 277px; height: 277px;
    background: var(--brand-blue);
  }
  .brand-mark {
    position: absolute; left: 0; width: 277px; top: 170px;
    display: flex; align-items: center; justify-content: center; gap: 10px;
    font-weight: 700; font-size: 36px; letter-spacing: 1px; line-height: 1;
  }
  .brand-mark__dot { width: 18px; height: 18px; border-radius: 50%; }
  .card--front-bold .brand-mark { color: var(--silver); }
  .card--front-bold .brand-mark__dot { background: var(--silver); }
  .card--front-quiet .brand-mark { color: var(--brand-navy); }
  .card--front-quiet .brand-mark__dot { background: var(--brand-navy); }

  .slogan-bold {
    position: absolute; left: 277px; top: 0;
    color: var(--brand-blue); font-weight: 700; text-transform: uppercase;
  }
  .slogan-bold span { position: absolute; left: 0; white-space: nowrap; line-height: 1; }
  .slogan-bold .s1 { top: 77px; font-size: 29px; letter-spacing: -0.2px; }
  .slogan-bold .s2 { top: 113px; font-size: 29px; letter-spacing: -0.2px; }
  .slogan-bold .s3 { top: 161px; font-size: 56px; letter-spacing: -0.5px; }
  .slogan-bold .s4 { top: 220px; font-size: 29px; letter-spacing: -0.2px; }

  .slogan-quiet { position: absolute; left: 302px; top: 168px; color: var(--brand-navy); }
  .slogan-quiet .line-small { display: block; font-size: 14px; line-height: 18px; }
  .slogan-quiet .line-large { display: block; font-size: 22px; letter-spacing: 1px; line-height: 30px; }

  .contact { position: absolute; left: 40px; }
  .contact__name { font-size: 13px; color: var(--brand-blue); }
  .contact__name strong { font-weight: 700; }
  .contact__post { font-size: 9px; color: var(--text-grey); margin-top: 18px; }
  .contact__list { list-style: none; margin-top: 22px; font-size: 13.5px; line-height: 17.5px; }
  .contact__list b { display: inline-block; width: 19px; color: var(--brand-blue); font-weight: 700; }
  .card--back-grey .contact { top: 68px; }
  .card--back-grey .contact__list { color: var(--ink-grey); }
  .card--back-navy .contact { top: 101px; }
  .card--back-navy .contact__post,
  .card--back-navy .contact__list { color: var(--brand-navy); }
  .card--back-navy .contact__post { margin-top: 15px; }
  .card--back-navy .contact__list { margin-top: 20px; }

  .mission { position: absolute; font-size: 13px; line-height: 17px; letter-spacing: 0.3px; }
  .card--back-grey .mission { left: 40px; top: 232px; color: var(--text-grey); }
  .card--back-navy .mission { left: 261px; top: 179px; color: var(--brand-navy); }
  .card--back-navy .mission .mission__second { font-size: 14px; }

  .back-mark {
    position: absolute; display: flex; align-items: center; gap: 8px;
    font-weight: 700; font-size: 24px; letter-spacing: 1px; line-height: 1;
  }
  .back-mark__dot { width: 14px; height: 14px; border-radius: 50%; }
  .card--back-grey .back-mark { left: 268px; top: 98px; color: var(--ink-grey); }
  .card--back-grey .back-mark__dot { background: var(--ink-grey); }
  .card--back-navy .back-mark { left: 265px; top: 98px; color: var(--brand-navy); }
  .card--back-navy .back-mark__dot { background: var(--brand-navy); }
</style>
</head>
<body>
<main class="sheet">

  <section class="card card--front-bold" aria-label="Business card front, bold slogan">
    <div class="brand-panel">
      <div class="brand-mark"><span class="brand-mark__dot"></span>QUORVIAL</div>
    </div>
    <p class="slogan-bold">
      <span class="s1">Measurable</span>
      <span class="s2">Marketing.</span>
      <span class="s3">Epic</span>
      <span class="s4">Results.</span>
    </p>
  </section>

  <section class="card card--front-quiet" aria-label="Business card front, quiet slogan">
    <div class="brand-panel">
      <div class="brand-mark"><span class="brand-mark__dot"></span>QUORVIAL</div>
    </div>
    <p class="slogan-quiet">
      <span class="line-small">Measurable Marketing.</span>
      <span class="line-large">Epic Results.</span>
    </p>
  </section>

  <section class="card card--back-grey" aria-label="Business card back, grey">
    <div class="contact">
      <p class="contact__name"><strong>Liam</strong> Harcourt</p>
      <p class="contact__post">B Bus. Mktg, Grad Dip Digital Mktg, CPM</p>
      <ul class="contact__list">
        <li><b>M</b>0400 555 019</li>
        <li><b>W</b>www.quorvial.com.au</li>
        <li><b>E</b>info@quorvial.com.au</li>
      </ul>
    </div>
    <div class="back-mark"><span class="back-mark__dot"></span>QUORVIAL</div>
    <p class="mission">Turning insights into action<br>and passion into profit.</p>
  </section>

  <section class="card card--back-navy" aria-label="Business card back, navy">
    <div class="contact">
      <p class="contact__name"><strong>Liam</strong> Harcourt</p>
      <p class="contact__post">B Bus. Mktg, Grad Dip Digital Mktg, CPM</p>
      <ul class="contact__list">
        <li><b>M</b>0400 555 019</li>
        <li><b>W</b>www.quorvial.com.au</li>
        <li><b>E</b>info@quorvial.com.au</li>
      </ul>
    </div>
    <div class="back-mark"><span class="back-mark__dot"></span>QUORVIAL</div>
    <p class="mission">Turning insights into action<br><span class="mission__second">and passion into profit.</span></p>
  </section>

</main>
</body>
</html>
```